We need letterhead, Business Cards, and envelops designed. We have attached a design of our logo and a sample of letterhead idea that was started but never perfected, it is only an idea for the letterhead if you can design something better we may love that also we are open to change.
We want a design that looks professional in style. we are a non profit trade association in the construction industry. the green color in the attached design represent green building, and we like that. also if you just want to enhance the letterhead sample that we attached that would be fine also.
Thanks and good luck
also the name that should show on the first business cards should be Merwin Haskell, Director are web address is www.vtqpa.org

```html
<!DOCTYPE html>
<html lang="en">
<head>
<meta charset="utf-8">
<title>VTQPA Stationery Set</title>
<link rel="stylesheet" href="https://fonts.googleapis.com/css2?family=Source+Sans+3:wght@400;600;700&family=Arimo:wght@400;700&display=swap">
<style>
  :root{
    --backdrop:#d6d6d6;
    --paper:#ffffff;
    --ink:#1f1f1f;
    --ink-soft:#444;
    --green-light:#8cc152;
    --green-mid:#6aa84f;
    --green-dark:#4a8344;
    --green-pale:#cfe6b6;
  }
  *{box-sizing:border-box;margin:0;padding:0}
  html,body{width:1200px;height:823px;overflow:hidden;background:var(--backdrop)}
  body{position:relative;font-family:"Source Sans 3",sans-serif;color:var(--ink)}
  .sheet{position:absolute;background:var(--paper);overflow:hidden}
  .bands{position:absolute;inset:0;width:100%;height:100%}
  .wordmark{position:absolute;display:flex;align-items:center;gap:.25em;font-family:"Source Sans 3",sans-serif;font-weight:600;color:var(--ink);line-height:1;letter-spacing:.02em}
  .wordmark .mark{display:block;width:.62em;height:.62em;background:var(--green-mid)}

  /* Letterhead */
  .letterhead{left:72px;top:58px;width:480px;height:705px}
  .letterhead .wordmark{left:38px;top:48px;font-size:40px}
  .contact{position:absolute;font-size:8.5px;line-height:1.3;text-transform:uppercase;color:var(--ink-soft)}
  .letterhead .contact{left:343px;top:60px;font-size:9px;text-transform:none}
  .letter{position:absolute;left:38px;top:137px;width:428px;font-size:9.2px;line-height:1.3}
  .letter p{margin-bottom:12px}
  .letter .gap{margin-top:38px}
  .letter-foot{position:absolute;left:38px;right:10px;top:677px;border-top:1px solid #333}
  .letter-url{position:absolute;right:14px;top:664px;font-size:9px;color:var(--ink-soft)}

  /* Envelopes */
  .envelope-front{left:622px;top:58px;width:503px;height:245px}
  .envelope-front .wordmark{left:34px;top:36px;font-size:30px}
  .envelope-front .contact{left:42px;top:208px;font-size:6px}
  .envelope-back{left:623px;top:355px;width:497px;height:237px}
  .envelope-back .wordmark{left:190px;top:24px;font-size:30px}

  /* Cards */
  .card-front{left:621px;top:643px;width:210px;height:116px}
  .card-front .wordmark{left:36px;top:48px;font-size:30px}
  .card-back{left:908px;top:646px;width:205px;height:113px}
  .card-back .wordmark{left:102px;top:18px;font-size:22px}
  .card-name{position:absolute;left:16px;top:46px;font-family:"Arimo",sans-serif;font-size:11px;color:var(--ink)}
  .card-role{position:absolute;left:16px;top:59px;font-family:"Arimo",sans-serif;font-size:7px;font-weight:700;font-style:italic;color:var(--ink)}
  .card-rule{position:absolute;left:16px;right:12px;top:71px;border-top:1px solid #bbb}
  .card-back .contact{right:12px;top:75px;font-size:5px;text-align:right;font-weight:700;color:var(--ink)}
  .card-back .card-url{position:absolute;right:12px;top:94px;font-size:5px;font-weight:700}
</style>
</head>
<body>

<section class="sheet letterhead">
  <div class="wordmark"><span class="mark"></span>VTQPA</div>
  <div class="contact">SUNDAY SERVICE, 9:30 AM<br>MAP &amp; DIRECTIONS<br>(555) 014-2290</div>
  <div class="letter">
    <p>2260, Alder Crest Road<br>Fairmont, CA 90410.</p>
    <p>January 29th, 2011</p>
    <p>Mr. Pellham<br>President, Pellham Youth Center<br>518 Orchard Row<br>Brookvale, NY 10380</p>
    <p>Dear Mr. Pellham:</p>
    <p>In the first paragraph, one needs to give a brief introduction of oneself. One should also give reference to the purpose of the letter in brief.<br>The second paragraph needs to give the details of the letter and its need. This paragraph is mostly longer than the others and plays the main role in the letter. Keep the sentences short and to the point. Avoid using complex words and sentences.</p>
    <p class="gap">The third and last paragraph is the conclusion of the letter and can be kept short.</p>
    <p>Sincerely,</p>
    <p>(this is where the signature of the writer will be placed)</p>
    <p>Noel Ardwick<br>Read more at Letterguide: http://www.letterguide.example/format-sample.html</p>
  </div>
  <div class="letter-url">www.vtqpa.org</div>
  <div class="letter-foot"></div>
</section>

<section class="sheet envelope-front">
  <svg class="bands" viewBox="0 0 503 245" preserveAspectRatio="none" aria-hidden="true">
    <polygon points="0,0 300,0 0,75" fill="var(--green-pale)"/>
    <polygon points="0,0 300,0 0,40" fill="var(--green-light)"/>
    <polygon points="150,245 503,200 503,245" fill="var(--green-pale)"/>
    <polygon points="230,245 503,208 503,245" fill="var(--green-light)"/>
    <polygon points="320,245 503,218 503,245" fill="var(--green-dark)"/>
  </svg>
  <div class="wordmark"><span class="mark"></span>VTQPA</div>
  <div class="contact">Sunday Service, 9:30 AM<br>Map &amp; Directions<br>(555) 014-2290</div>
</section>

<section class="sheet envelope-back">
  <svg class="bands" viewBox="0 0 497 237" preserveAspectRatio="none" aria-hidden="true">
    <polygon points="0,0 497,0 485,75 0,75" fill="#fafafa"/>
    <polygon points="0,0 270,0 0,90" fill="var(--green-pale)"/>
    <polygon points="0,0 270,0 0,52" fill="var(--green-light)"/>
    <line x1="0" y1="76" x2="485" y2="76" stroke="#ccc" stroke-width="1"/>
    <line x1="485" y1="76" x2="497" y2="0" stroke="#ccc" stroke-width="1"/>
    <polygon points="150,237 497,198 497,237" fill="var(--green-pale)"/>
    <polygon points="240,237 497,206 497,237" fill="var(--green-light)"/>
    <polygon points="330,237 497,214 497,237" fill="var(--green-dark)"/>
  </svg>
  <div class="wordmark"><span class="mark"></span>VTQPA</div>
</section>

<section class="sheet card-front">
  <svg class="bands" viewBox="0 0 210 116" preserveAspectRatio="none" aria-hidden="true">
    <polygon points="0,0 180,0 0,38" fill="var(--green-pale)"/>
    <polygon points="0,0 180,0 0,22" fill="var(--green-light)"/>
    <polygon points="40,116 210,88 210,116" fill="var(--green-pale)"/>
    <polygon points="80,116 210,94 210,116" fill="var(--green-light)"/>
    <polygon points="120,116 210,102 210,116" fill="var(--green-dark)"/>
  </svg>
  <div class="wordmark"><span class="mark"></span>VTQPA</div>
</section>

<section class="sheet card-back">
  <svg class="bands" viewBox="0 0 205 113" preserveAspectRatio="none" aria-hidden="true">
    <polygon points="0,0 90,0 0,26" fill="var(--green-pale)"/>
    <polygon points="0,0 90,0 0,14" fill="var(--green-light)"/>
  </svg>
  <div class="wordmark"><span class="mark"></span>VTQPA</div>
  <div class="card-name">Merwin Haskell</div>
  <div class="card-role">Director</div>
  <div class="card-rule"></div>
  <div class="contact">Sunday Service, 9:30 AM<br>Map &amp; Directions<br>(555) 014-2290</div>
  <div class="card-url">www.vtqpa.org</div>
</section>

</body>
</html>
```